British Columbia Day banner showcasing 20% off site

Banner graphic promoting our BC Day sale
Size: 1800 x 1000
- flag has been uploaded for inspiration
- examples from other companies and their sale banners have been uploaded for inspiration.
- product images can be found at www.mygreenleafhub.com, please use a variety of different products in this banner

Target Market(s)

19+

Industry/Entity Type

Cannabis

Requirements
Must have
• Phrases:
- “Celebrate BC Day with BC bud and companies”
- “20% off site wide sale*"
- Underneath phrase the date of sale “July 30th - August 3rd”
- In tiny print “*excludes all sale and bundled items”
- MUST BE 1800 X1000
Nice to have
• - images of the products or bud we carry which can be found at www.mygreenleafhub.com
- bold
Should not have
• - company logo

```html
<!DOCTYPE html>
<html lang="en">
<head>
<meta charset="utf-8">
<title>BC Day Sale Banner</title>
<link rel="stylesheet" href="https://fonts.googleapis.com/css2?family=Archivo:wght@500;600;700&family=Chivo:wght@700;800&family=Gelasio:wght@700&display=swap">
<style>
  :root {
    --paper: #e0d8c8;
    --red: #c03033;
    --green: #1a5a18;
    --deep-green: #1e6f2c;
    --ink: #111111;
    --leaf-ink: #2c4a38;
  }
  * { margin: 0; padding: 0; box-sizing: border-box; }
  html, body { width: 1200px; height: 667px; overflow: hidden; background: var(--paper); }
  .banner {
    position: relative;
    width: 1200px;
    height: 667px;
    background: var(--paper);
    overflow: hidden;
    font-family: "Archivo", sans-serif;
  }
  .leaf-art {
    position: absolute;
    left: 580px;
    top: 0;
    width: 620px;
    height: 667px;
  }
  .headline {
    position: absolute;
    left: 58px;
    top: 134px;
    color: var(--red);
    font-family: "Chivo", sans-serif;
    font-weight: 700;
    font-size: 69px;
    line-height: 80px;
    letter-spacing: 0.5px;
    white-space: nowrap;
  }
  .offer {
    position: absolute;
    left: 60px;
    top: 304px;
    display: flex;
    align-items: baseline;
    color: var(--ink);
    white-space: nowrap;
  }
  .offer-number {
    font-family: "Chivo", sans-serif;
    font-weight: 800;
    font-size: 90px;
    line-height: 1;
    color: var(--deep-green);
    letter-spacing: -2px;
  }
  .offer-percent {
    font-family: "Gelasio", serif;
    font-weight: 700;
    font-size: 26px;
    margin-left: 16px;
  }
  .offer-off {
    font-family: "Gelasio", serif;
    font-weight: 700;
    font-size: 38px;
    margin-left: 6px;
  }
  .offer-text {
    font-family: "Chivo", sans-serif;
    font-weight: 700;
    font-size: 43px;
    margin-left: 20px;
  }
  .dates {
    position: absolute;
    left: 61px;
    top: 426px;
    color: var(--green);
    font-family: "Chivo", sans-serif;
    font-weight: 700;
    font-size: 33px;
    white-space: nowrap;
  }
  .dates-rule {
    position: absolute;
    left: 61px;
    top: 477px;
    width: 348px;
    height: 2px;
    background: var(--green);
  }
  .fine-print {
    position: absolute;
    left: 61px;
    top: 501px;
    color: var(--ink);
    font-size: 16px;
    font-weight: 500;
    white-space: nowrap;
  }
</style>
</head>
<body>
  <main class="banner">
    <svg class="leaf-art" viewBox="0 0 620 667" role="img" aria-label="Hand-drawn illustration of two large cannabis leaves in dark green ink, one rising at the top right and one at the bottom">
      <defs>
        <radialGradient id="leafUpper" cx="0.5" cy="0.5" r="0.5">
          <stop offset="0" stop-color="#2c4a38" stop-opacity="0.55"/>
          <stop offset="0.6" stop-color="#2c4a38" stop-opacity="0.28"/>
          <stop offset="1" stop-color="#2c4a38" stop-opacity="0"/>
        </radialGradient>
        <radialGradient id="leafLower" cx="0.5" cy="0.5" r="0.5">
          <stop offset="0" stop-color="#2c4a38" stop-opacity="0.5"/>
          <stop offset="0.6" stop-color="#2c4a38" stop-opacity="0.25"/>
          <stop offset="1" stop-color="#2c4a38" stop-opacity="0"/>
        </radialGradient>
      </defs>
      <ellipse cx="480" cy="330" rx="190" ry="340" fill="url(#leafUpper)"/>
      <ellipse cx="215" cy="540" rx="230" ry="190" fill="url(#leafLower)"/>
    </svg>

    <h1 class="headline">Celebrate BC Day with<br>BC bud and companies</h1>

    <div class="offer">
      <span class="offer-number">20</span>
      <span class="offer-percent">%</span>
      <span class="offer-off">Off</span>
      <span class="offer-text">site wide sale</span>
    </div>

    <p class="dates">July 30th - August 3rd</p>
    <div class="dates-rule"></div>

    <p class="fine-print">*excludes all sale and bundled items</p>
  </main>
</body>
</html>
```